Business Card Design for Portrait photography professional

We are a small company specializing in portrait photography (weddings, family, couples, children, newborn, pregnant, etc.) Occasionally we do business portraits too and do some other type of photography. We need a business card which would fit into the same look and feel as our website theme (lumvika.com - under construction currently).
Our target customer base lies within mid- to upmarket. We want our business cards to convey a feeling of quality, solidness and a bit luxury.
Design should be universal and usable on 85mmx55mm, 90mmx50mm and 90mmx55mm
one extra file (PSD of a website didn't fit into the allowed updoad, therefore has put it into my filecrate: https://www.filecrate-example.net/s/qt7wk2rbvx9dmhe/website%20theme%20PSD.psd)

Target Market(s)

mostly private people, 25-60 years old, mostly well established.

Industry/Entity Type

Portrait Photography

Requirements
Must have
• 2 sided design (print on both sides of the business card).
Must include:
business name, logo, URL (lumvika.no) , employee name, email address, and phone number.
Colorscheme of the website lumvika.no / lumvika.com

```html
<!DOCTYPE html>
<html lang="en">
<head>
<meta charset="utf-8">
<title>Lumvika – Business Card</title>
<link rel="stylesheet" href="https://fonts.googleapis.com/css2?family=Quicksand:wght@300;400;500&display=swap">
<style>
  :root {
    --page-bg: #eef2f5;
    --card-dark: #0b0d0e;
    --card-glow: #2b3033;
    --text-main: #b9c2c4;
    --text-soft: #98a2a5;
    --divider-hi: #3a4043;
    --divider-lo: #050606;
    --icon: #aab3b5;
  }
  * { box-sizing: border-box; margin: 0; padding: 0; }
  html, body { width: 1200px; height: 1000px; overflow: hidden; }
  body {
    background: var(--page-bg);
    font-family: "Quicksand", sans-serif;
    position: relative;
  }
  .card {
    position: absolute;
    width: 630px;
    height: 360px;
    background: radial-gradient(ellipse 55% 60% at 50% 50%, var(--card-glow) 0%, #17191b 55%, var(--card-dark) 100%);
    box-shadow: 2px 3px 5px rgba(0,0,0,0.35);
    color: var(--text-main);
  }
  .card--front { left: 104px; top: 100px; }
  .card--back  { left: 455px; top: 557px; height: 358px; }
  .divider {
    position: absolute;
    width: 2px;
    border-left: 1px solid var(--divider-lo);
    border-right: 1px solid var(--divider-hi);
    opacity: 0.8;
  }
  .card--front .divider { left: 339px; top: 110px; height: 170px; }
  .card--back .divider  { left: 338px; top: 100px; height: 172px; }

  .business-name {
    position: absolute;
    right: 307px; top: 158px;
    font-weight: 300;
    font-size: 21px;
    letter-spacing: 0.3px;
    white-space: nowrap;
  }
  .business-url {
    position: absolute;
    right: 307px; top: 188px;
    font-size: 10.5px;
    letter-spacing: 0.6px;
    color: var(--text-soft);
  }
  .brand-mark {
    position: absolute;
    left: 360px; top: 91px;
    width: 176px; height: 176px;
    border: 2px solid var(--text-main);
    border-radius: 50%;
    display: flex; align-items: center; justify-content: center;
  }
  .brand-mark__name {
    font-weight: 400;
    font-size: 24px;
    letter-spacing: 3px;
    color: #d8dee0;
  }

  .contact-list {
    position: absolute;
    right: 302px; top: 132px;
    list-style: none;
    text-align: right;
    font-size: 12px;
    line-height: 24.7px;
  }
  .contact-icons {
    position: absolute;
    left: 353px; top: 135px;
    list-style: none;
  }
  .contact-icons li { height: 24.7px; display: flex; align-items: center; }
  .contact-icons svg { width: 18px; height: 14px; fill: var(--icon); }
  .employee {
    position: absolute;
    left: 394px; top: 161px;
  }
  .employee__name { font-size: 14px; letter-spacing: 0.4px; }
  .employee__role { font-size: 11px; letter-spacing: 0.4px; color: var(--text-soft); margin-top: 2px; }
</style>
</head>
<body>

<section class="card card--front">
  <h1 class="business-name">PERSONAL PHOTOGRAPHER</h1>
  <p class="business-url">WWW.LUMVIKA.COM</p>
  <div class="divider"></div>
  <div class="brand-mark"><span class="brand-mark__name">LUMVIKA</span></div>
</section>

<section class="card card--back">
  <ul class="contact-list">
    <li>555 555 5555</li>
    <li>Your Address</li>
    <li>Yourmail@webpage.com</li>
    <li>Chirpline.com/YourName</li>
  </ul>
  <div class="divider"></div>
  <ul class="contact-icons">
    <li><svg viewBox="0 0 18 14" aria-label="Phone"><path d="M1 3c2-2 14-2 16 0l0 2-4 0 0-1.5c-2-.6-6-.6-8 0L5 5 1 5z"/><rect x="4" y="6" width="10" height="7" rx="1"/></svg></li>
    <li><svg viewBox="0 0 18 14" aria-label="Address"><path d="M9 0a4.5 4.5 0 0 0-4.5 4.5C4.5 8 9 14 9 14s4.5-6 4.5-9.5A4.5 4.5 0 0 0 9 0zm0 6.3a1.8 1.8 0 1 1 0-3.6 1.8 1.8 0 0 1 0 3.6z"/></svg></li>
    <li><svg viewBox="0 0 18 14" aria-label="Email"><path d="M1 2h16v10H1z M2 3l7 5 7-5" fill="none" stroke="#aab3b5" stroke-width="1.5"/></svg></li>
    <li><svg viewBox="0 0 18 14" aria-label="Social profile"><circle cx="9" cy="7" r="6"/></svg></li>
  </ul>
  <div class="employee">
    <p class="employee__name">EMPLOYEE NAME</p>
    <p class="employee__role">EMPLOYEE ROLE</p>
  </div>
</section>

</body>
</html>
```